New Menu Design Projet for beach town downtown Lounge

I am looking for a redesign of my cocktail menu (12 pages), dinner(2 pages) and wine list(1 page), Late night Menu (1 page) as well as a 2 promo posters (11 x 17) designed for flyers and posting around town and menu board for our front (17 x 23)

I will include examples of stuff that I like and previous work we’ve had done for us.
The final design I want to have some unity and branding with our logo possibly slightly reworked and updated. I want there to be a large focus of highlighting the features and making them pop off the page and get peoples attention. I also want their to be a focus on legibility and being able to read the menus as we get to be a dark lounge at night and lots of notice that the kitchen is open late.

19-50

Town

Sans Serif

• Good spacing, clean simple look, not cheesy or tacky. Please read the full brief under File 1 it is a word document with much more details.
• You can also reach me to ask questions as well at mel@harbor817.com or through pitch loft
• light back ground and dark font, i disliked the black background and light writing it was very difficult to read

```html
<!DOCTYPE html>
<html lang="en">
<head>
<meta charset="utf-8">
<title>Harbor's Dinner Menu</title>
<link href="https://fonts.googleapis.com/css2?family=Raleway:ital,wght@0,300;0,400;0,500;0,700;1,300;1,400&display=swap" rel="stylesheet">
<style>
  :root{
    --paper:#f6eee2;
    --paper-edge:#e9d9c2;
    --heading:#4b4745;
    --item:#9c2b2d;
    --text:#5b5754;
    --muted:#77716b;
    --rule:#a9a39c;
    --node:#8e2a2b;
  }
  *{margin:0;padding:0;box-sizing:border-box}
  html,body{width:927px;height:1200px;overflow:hidden}
  body{
    font-family:"Raleway",sans-serif;
    color:var(--text);
    background:radial-gradient(ellipse at 50% 45%,#fbf6ee 0%,var(--paper) 55%,var(--paper-edge) 100%);
    position:relative;
  }
  .menu{position:relative;width:927px;height:1200px}
  .section-title{
    position:absolute;font-weight:700;font-size:21px;letter-spacing:1px;
    color:var(--heading);transform:translateX(-50%);white-space:nowrap;line-height:1;
  }
  .section-note{
    position:absolute;font-style:italic;font-weight:300;font-size:13px;line-height:17px;
    color:var(--muted);text-align:center;transform:translateX(-50%);
  }
  .item{position:absolute;width:402px}
  .item-name{
    font-weight:500;font-size:15px;letter-spacing:.4px;color:var(--item);
    text-transform:uppercase;line-height:18px;margin-bottom:3px;
  }
  .item-line{font-weight:300;font-size:14px;line-height:18px;white-space:nowrap}
  .item-line.last{display:flex;align-items:baseline}
  .leader{flex:1;border-bottom:2px dotted var(--rule);margin:0 3px;transform:translateY(-3px)}
  .price{font-weight:400;color:var(--heading)}
  .addon{font-style:italic;font-weight:300;font-size:13px;line-height:18px}
  .rule-h{position:absolute;height:0;border-top:3px dotted var(--rule)}
  .rule-v{position:absolute;width:0;border-left:3px dotted var(--rule)}
  .node{position:absolute;width:8px;height:8px;border-radius:50%;background:var(--node);transform:translate(-50%,-50%)}
  .footnote{
    position:absolute;left:463px;top:1139px;transform:translateX(-50%);
    font-style:italic;font-weight:300;font-size:13px;color:var(--muted);white-space:nowrap;
  }
</style>
</head>
<body>
<main class="menu">

  <div class="rule-v" style="left:467px;top:14px;height:386px"></div>
  <div class="rule-v" style="left:467px;top:412px;height:405px"></div>
  <div class="rule-h" style="left:33px;top:404px;width:856px"></div>
  <div class="rule-h" style="left:33px;top:821px;width:856px"></div>
  <div class="node" style="left:469px;top:406px"></div>
  <div class="node" style="left:469px;top:823px"></div>

  <!-- Steaks -->
  <h2 class="section-title" style="left:234px;top:32px">STEAKS</h2>
  <p class="section-note" style="left:234px;top:62px;width:420px">All cuts aged and butchered in house, served with seasonal<br>vegetables, loaded baked potato, and onion ring</p>

  <div class="item" style="left:33px;top:117px">
    <h3 class="item-name">Signature Creole Flatiron</h3>
    <p class="item-line">Papaya marinated blackened flatiron served with</p>
    <p class="item-line last">chimmi churri sauce<span class="leader"></span><span class="price">24</span></p>
  </div>
  <div class="item" style="left:33px;top:186px">
    <h3 class="item-name">10 oz N.Y. Striploin</h3>
    <p class="item-line last">Okanagan red wine and veal demi glace<span class="leader"></span><span class="price">30</span></p>
  </div>
  <div class="item" style="left:33px;top:241px">
    <h3 class="item-name">Surf &amp; Turf</h3>
    <p class="item-line">8 oz. N.Y. stip loin topped with sauteed tiger prawns &amp;</p>
    <p class="item-line last">truffle butter<span class="leader"></span><span class="price">32</span></p>
  </div>
  <div class="item" style="left:33px;top:321px">
    <h3 class="item-name">Prime Rib</h3>
    <p class="item-line">10 oz. slow roasted prime AAA primerib, house au jus,</p>
    <p class="item-line last">duck confit yorkshire pudding<span class="leader"></span><span class="price">30</span></p>
  </div>

  <!-- Seafood -->
  <h2 class="section-title" style="left:684px;top:32px">SEAFOOD</h2>
  <p class="section-note" style="left:684px;top:62px;width:420px">Seafood served with wild and basmati rice blend,<br>seasonal vegetables, fresh lemon, leek tempura</p>

  <div class="item" style="left:490px;top:117px">
    <h3 class="item-name">Wild Salmon</h3>
    <p class="item-line">Okanagan wine poached wild BC salmon with</p>
    <p class="item-line last">artichoke and spinach buerre blanc<span class="leader"></span><span class="price">25</span></p>
  </div>
  <div class="item" style="left:490px;top:223px">
    <h3 class="item-name">Marlin</h3>
    <p class="item-line">Proscuitto wrapped with Okanagan peach chutney,</p>
    <p class="item-line last">white wine buerre blanc<span class="leader"></span><span class="price">25</span></p>
  </div>
  <div class="item" style="left:490px;top:336px">
    <h3 class="item-name">Ahi Tuna</h3>
    <p class="item-line last">Peppercorn crusted, papaya salsa, balsamic glaze<span class="leader"></span><span class="price">28</span></p>
  </div>

  <!-- Farm -->
  <h2 class="section-title" style="left:234px;top:427px">FARM</h2>
  <p class="section-note" style="left:234px;top:466px;width:420px">Served with duck fat roasted baby<br>potatos and seasonal vegetables</p>

  <div class="item" style="left:33px;top:519px">
    <h3 class="item-name">Okanagan Chicken</h3>
    <p class="item-line">Oven roasted chicken breast, Okanagan goat cheese &amp;</p>
    <p class="item-line last">stone dijon cream sauce<span class="leader"></span><span class="price">23</span></p>
  </div>
  <div class="item" style="left:33px;top:627px">
    <h3 class="item-name">Harbor's Baby Back Ribs</h3>
    <p class="item-line">Fullrack of fall off the bone baby back ribs, topped</p>
    <p class="item-line last">with house made peach bourbon bbq sauce<span class="leader"></span><span class="price">24</span></p>
  </div>
  <div class="item" style="left:33px;top:727px">
    <h3 class="item-name">Stuffed Pepper *vegan</h3>
    <p class="item-line">Quinoa stuffed, Fieldleaf Cheese, caramelized vegetables</p>
    <p class="item-line last">and chimmi churri<span class="leader"></span><span class="price">16</span></p>
  </div>

  <!-- Pasta bowls -->
  <h2 class="section-title" style="left:684px;top:427px">PASTA BOWLS</h2>

  <div class="item" style="left:490px;top:465px">
    <h3 class="item-name">Fettuccine Carbonara</h3>
    <p class="item-line">Crispy Italian bacon, roast garlic, and rosemary with</p>
    <p class="item-line last">herb broth &amp; cream<span class="leader"></span><span class="price">14.50</span></p>
    <p class="addon">Cajun Chicken / Add 6 • Gluten Free Pasta / Add 2.50</p>
  </div>
  <div class="item" style="left:490px;top:555px">
    <h3 class="item-name">Crab Gnocchi</h3>
    <p class="item-line">BC Dungeness crab, prawns and handmade gnocchi</p>
    <p class="item-line">tossed with pesto, lemon, white wine, italian bacon</p>
    <p class="item-line last">and roma Tomato<span class="leader"></span><span class="price">23.75</span></p>
  </div>
  <div class="item" style="left:490px;top:648px">
    <h3 class="item-name">Jambalaya Rice Bowl</h3>
    <p class="item-line">Chicken, chorizo, and prawns sautéed in a sambucca and</p>
    <p class="item-line last">cajun tomato sauce with basil &amp; red peppers<span class="leader"></span><span class="price">17</span></p>
  </div>
  <div class="item" style="left:490px;top:727px">
    <h3 class="item-name">Yellow Curry Rice Bowl</h3>
    <p class="item-line">Grilled Chicken with coconut yellow curry, peppers,</p>
    <p class="item-line last">seasonal veg and topped with peach chutney<span class="leader"></span><span class="price">17</span></p>
  </div>

  <!-- Sandwiches -->
  <h2 class="section-title" style="left:463px;top:851px">SANDWICHES</h2>
  <p class="section-note" style="left:463px;top:881px;width:520px">Served with house cut fries Substitute caeser salad, mixed<br>greens or yam fries for 2 or poutine for 4</p>

  <div class="item" style="left:33px;top:941px">
    <h3 class="item-name">Seafoodhouse Burger</h3>
    <p class="item-line">House ground AAA patty, bacon, smoked gouda</p>
    <p class="item-line last">cheese, blackberry relish<span class="leader"></span><span class="price">15</span></p>
  </div>
  <div class="item" style="left:33px;top:1029px">
    <h3 class="item-name">Southern Fried Chicken Sandwich</h3>
    <p class="item-line">Marinated in hot sauce and fried crispy, with lettuce,</p>
    <p class="item-line last">tomato, mayo on a brioche bun<span class="leader"></span><span class="price">14</span></p>
  </div>
  <div class="item" style="left:490px;top:941px">
    <h3 class="item-name">The Mushroom Burger</h3>
    <p class="item-line">House ground AAA patty, with fried mushrooms,</p>
    <p class="item-line last">bacon, aged cheddar and garlic butter<span class="leader"></span><span class="price">16</span></p>
  </div>
  <div class="item" style="left:490px;top:1029px">
    <h3 class="item-name">Steak Sandwich</h3>
    <p class="item-line">8oz flatiron steak sandwich topped with onion ring,</p>
    <p class="item-line last">red wine demi glace<span class="leader"></span><span class="price">19.50</span></p>
  </div>

  <p class="footnote">Groups 8 or larger are subject to %18 gratuity</p>
</main>
</body>
</html>
```